Pellow Studio Website Design

Home page & interior page design.

Target Market(s)

Small businesses or at home businesses. Budget $1,000 - $3,000.

Industry/Entity Type

Media

Number of Pages Required

2 pages

Requirements
Must have
• Home page must consist of:
- Logo in top left
- Bannerimagery showcasing design examples (to be provided)
- 4 main modules, directing users to the 4 main product areas:
1. Templated brochure websites
2. Custom designed brochure websites
3. eCommerce websites
4. SEO

Area for text to be inserted (around 200 words) of introductory text

- Use of correct colour pallette based on logo provided
Nice to have
• Custom designed icons for the 4 main product areas.
Should not have
• Unstructured, cluttered layout

```html
<!DOCTYPE html>
<html lang="en">
<head>
<meta charset="utf-8">
<title>Pellow Studio – Home</title>
<link rel="stylesheet" href="https://fonts.googleapis.com/css2?family=Ubuntu:wght@400;500;700&family=PT+Sans:wght@400;700&family=Noto+Sans+Mono:wght@700&display=swap">
<style>
  :root{
    --red:#d42027;
    --orange:#f28c1c;
    --yellow:#f5c215;
    --ink:#1d1d1d;
    --white:#ffffff;
    --divider:#d42027;
  }
  *{margin:0;padding:0;box-sizing:border-box}
  html,body{width:1200px;height:800px;overflow:hidden;background:var(--white)}
  .page{position:relative;width:1200px;height:800px;overflow:hidden;font-family:"PT Sans",sans-serif;color:var(--ink)}

  .brand{position:absolute;left:22px;top:26px;display:flex;align-items:center;gap:12px}
  .brand-dot{width:22px;height:22px;border-radius:50%;background:var(--red)}
  .brand-name{font-family:"Ubuntu",sans-serif;font-weight:700;font-size:50px;color:var(--orange);letter-spacing:-1px}

  .note{position:absolute;font-family:"Ubuntu",sans-serif;font-weight:700;color:var(--red);white-space:nowrap}
  .note-hover{left:553px;top:54px;font-size:19px}
  .note-image{left:999px;top:373px;font-size:20px}

  .main-nav{position:absolute;left:600px;top:91px;display:flex}
  .main-nav a{display:block;height:32px;width:140px;border-radius:12px 12px 0 0;background:var(--yellow);
    font-family:"Ubuntu",sans-serif;font-weight:700;font-size:18px;color:var(--ink);text-decoration:none;
    text-align:center;line-height:36px;white-space:nowrap}
  .main-nav a.is-active{background:var(--red);color:var(--white);height:38px;line-height:40px}
  .main-nav a:nth-child(4){width:138px}
  .top-rule{position:absolute;left:0;top:122px;width:1200px;height:7px;background:var(--red)}

  .hero-divider{position:absolute;left:599px;top:129px;width:2px;height:298px;background:var(--divider)}

  .intro{position:absolute;left:24px;top:157px;width:560px}
  .intro h1{font-family:"Ubuntu",sans-serif;font-weight:400;font-size:21px;margin-bottom:10px;white-space:nowrap}
  .intro p{font-weight:700;font-size:16px;line-height:19.5px;white-space:nowrap}

  .showcase{position:absolute;top:169px;height:200px;width:202px}
  .showcase-one{left:677px;background:linear-gradient(135deg,#1a0d2c 0%,#6b1d6a 35%,#e3502a 60%,#f6c313 80%,#1a1a1a 100%);border:1px solid #999}
  .showcase-two{left:927px;height:194px;width:200px;background:linear-gradient(160deg,#2a3947 0%,#3f5e78 40%,#b48a4a 60%,#263442 100%);border:1px solid #888}

  .services-band{position:absolute;left:0;top:460px;width:1200px;height:73px}
  .services-band .band-orange{position:absolute;left:0;top:0;width:1200px;height:16px;background:var(--orange)}
  .services-band .band-red{position:absolute;left:0;top:16px;width:1200px;height:57px;background:var(--red)}

  .service-icon{position:absolute;top:425px;width:98px;height:112px}
  .service-title{position:absolute;font-family:"Ubuntu",sans-serif;font-weight:700;font-size:20px;line-height:26px;color:var(--white);white-space:nowrap}

  .col-rule{position:absolute;top:533px;width:2px;height:267px;background:var(--divider)}
  .service-text{position:absolute;top:551px;font-family:"Noto Sans Mono",monospace;font-weight:700;font-size:13px;letter-spacing:-0.4px;line-height:22px;white-space:nowrap}
</style>
</head>
<body>
<div class="page">

  <div class="brand"><span class="brand-name">Pellow Studio</span><span class="brand-dot"></span></div>

  <span class="note note-hover">On Mouse over</span>

  <nav class="main-nav">
    <a class="is-active" href="#">Home</a>
    <a href="#">Servcies</a>
    <a href="#">Portfolio</a>
    <a href="#">Contact Us</a>
  </nav>
  <div class="top-rule"></div>
  <div class="hero-divider"></div>

  <section class="intro">
    <h1>Welcome to Pellow Studio</h1>
    <p>This site provides web page templates which are nice looking,<br>professional and can be used free for personal and business<br>websites. Whether you don't know how to design a web page or are<br>in a hurry to get a site up, my templates are the perfect solution.<br>All templates and graphics on this site are original &nbsp;I have only one<br>rule that you must follow, so before youget started using my<br>templates and graphics.</p>
  </section>

  <div class="showcase showcase-one" role="img" aria-label="Design example: dark website template with colourful flowing light waves"></div>
  <div class="showcase showcase-two" role="img" aria-label="Design example: blue business website template with a globe banner"></div>
  <span class="note note-image">Image here</span>

  <div class="services-band"><div class="band-orange"></div><div class="band-red"></div></div>

  <svg class="service-icon" style="left:-4px" viewBox="0 0 98 112" aria-hidden="true">
    <polygon points="4,4 94,4 49,108" fill="var(--orange)" stroke="#fff" stroke-width="3"/>
    <rect x="30" y="22" width="26" height="22" fill="none" stroke="#fff" stroke-width="3"/>
    <rect x="40" y="32" width="26" height="22" fill="#fff" opacity=".85"/>
  </svg>
  <div class="service-title" style="left:91px;top:477px">Templated<br>brochure websites</div>

  <svg class="service-icon" style="left:274px" viewBox="0 0 98 112" aria-hidden="true">
    <polygon points="4,4 94,4 49,108" fill="var(--orange)" stroke="#fff" stroke-width="3"/>
    <g stroke="#fff" stroke-width="4" stroke-linecap="round" fill="none">
      <line x1="36" y1="22" x2="48" y2="56"/>
      <circle cx="35" cy="21" r="6"/>
      <line x1="62" y1="24" x2="52" y2="56"/>
      <line x1="54" y1="22" x2="70" y2="28"/>
    </g>
  </svg>
  <div class="service-title" style="left:368px;top:481px">Custom designed<br>brochure websites</div>

  <svg class="service-icon" style="left:602px" viewBox="0 0 98 112" aria-hidden="true">
    <polygon points="4,4 94,4 49,108" fill="var(--orange)" stroke="#fff" stroke-width="3"/>
    <polyline points="26,22 33,22 39,46 64,46 69,28 35,28" stroke="#fff" stroke-width="3.5" fill="none" stroke-linejoin="round"/>
    <circle cx="42" cy="54" r="3.5" fill="#fff"/>
    <circle cx="61" cy="54" r="3.5" fill="#fff"/>
  </svg>
  <div class="service-title" style="left:692px;top:484px">eCommerce websites</div>

  <svg class="service-icon" style="left:909px" viewBox="0 0 98 112" aria-hidden="true">
    <polygon points="4,4 94,4 49,108" fill="var(--orange)" stroke="#fff" stroke-width="3"/>
    <g stroke="#fff" stroke-width="3" fill="none">
      <circle cx="44" cy="34" r="13"/>
      <ellipse cx="44" cy="34" rx="5.5" ry="13"/>
      <line x1="31" y1="34" x2="57" y2="34"/>
      <line x1="54" y1="44" x2="66" y2="56" stroke-width="5" stroke-linecap="round"/>
    </g>
  </svg>
  <div class="service-title" style="left:999px;top:488px">SEO</div>

  <div class="col-rule" style="left:297px"></div>
  <div class="col-rule" style="left:602px"></div>
  <div class="col-rule" style="left:909px"></div>

  <p class="service-text" style="left:21px">jdashgdhsghldshgjhdfsflkdsjgklj<br>skldgjkldfsjgkljdgkldsjklgjskldjg<br>sdgkjfkldsnklgnkldsngklnsdlfgfh<br>mdsgkjkjkfjkfdjklkldfnkldfklhfd<br>kdsgkfjkjfdkjkfdjkhjfkh;ldfk;gl</p>
  <p class="service-text" style="left:331px">jdashgdhsghldshgjhdfsflkdsjgklj<br>skldgjkldfsjgkljdgkldsjklgjskldjg<br>sdgkjfkldsnklgnkldsngklnsdlfgfh<br>mdsgkjkjkfjkfdjklkldfnkldfklhfd<br>kdsgkfjkjfdkjkfdjkhjfkh;ldfk;gl</p>
  <p class="service-text" style="left:625px">jdashgdhsghldshgjhdfsflkdsjgklj<br>skldgjkldfsjgkljdgkldsjklgjskldjg<br>sdgkjfkldsnklgnkldsngklnsdlfgfh<br>mdsgkjkjkfjkfdjklkldfnkldfklhfd<br>kdsgkfjkjfdkjkfdjkhjfkh;ldfk;gl</p>
  <p class="service-text" style="left:937px">jdashgdhsghldshgjhdfsflkdsjgklj<br>skldgjkldfsjgkljdgkldsjklgjskldjg<br>sdgkjfkldsnklgnkldsngklnsdlfgfh<br>mdsgkjkjkfjkfdjklkldfnkldfklhfd<br>kdsgkfjkjfdkjkfdjkhjfkh;ldfk;gl</p>

</div>
</body>
</html>
```